Buch-/eBook-Cover zum Thema Selbstverwirklichung
Zielgruppe
Titel des Buches: Der leise Kompass
Inhalt: Wir kennen es alle, in jungen Jahren ist alles neu, aufregend, wild und laut - das vergleiche ich im Buch mit vielen verspielten/tobenden/verrückten Monkeys, die sich einfach ausleben möchten und dabei noch weit sind von Selbstreflexion und bewussten Entscheidungen. Wir leben in den Tag hinein, haben einfach Spaß und eines Tages kommen wir an den Punkt, an dem wir uns eine Frage stellen: Wozu mache ich das eigentlich? Um andere zu beeindrucken? Wohin möchte ich eigentlich? Was gibt mir Sinn und Bedeutung? Auf was möchte ich am Ende meines Lebens mit einem Lächeln zurückblicken. Mit fortlaufender Lebensdauer werden wir ruhiger und unser innerer Monk lässt uns mehr/intensiver reflektieren à la „welche Richtung möchte ich einschlagen?“ und die Selbstverwirklichung steht im Vordergrund. Sollte sie zumindest stehen… dazu möchte ich den Leser inspirieren. Weniger auf externe Vergleiche achten, besser kommunizieren, Erfahrungen in positivem Maße nutzen, bewusstere Entscheidungen treffen, förderliche Gewohnheiten zu etablieren, das eigene Schicksal in die Hand nehmen, mit Liebe (sich selbst gegenüber und) der Umwelt begegnen und das persönliche individuelle Glück leben.
All das hat meine Welt bis dato geprägt und ich möchte genau das mit dem Leser teilen. Bei genauen Fragen zum Inhalt bitte einfach melden.
Hintergrund: Ich befinde mich aktuell auf Weltreise und habe dabei aus einem spontanen Gedanken heraus das Buch geschrieben. Zielgruppe sind diejenigen Leser, die sich gerne inspirieren lassen und auf einfache Lesekost stehen - keine spezielle Zielgruppe im Blick, mir geht es um Inspiration.
Aufgabenstellung
Hallo liebe(r) Designer/-in, ich hoffe mein Projekt spricht dich an und du teilst die Energie, die ich seit einigen Wochen in das Buch stecke. Also gehen wir‘s an!!
Die Schrift (Titel + Autorenname) soll auf jeden Fall blau sein und das Cover auf weißem Hintergrund entstehen. Es sollte ähnliche Komponenten enthalten, wie es die Beispielbilder zeigen:
- 1x Weltkugel (gerne in kräftigen Farbtönen) oder eine weitere Assoziationen mit dem Thema Weltreise/Weltkugel/Weltkarte bzw. „durch die Welt gehen”
- 1x Mönch mit orangener Robe > dabei einige lebendige Affen um ihn herum (manche verspielt/verträumt/tobend, manche dem Mönch zuhörend)
Das Design soll bitte allgemein „leichte Kost“ für das Auge sein und schlicht inspirierend/einladend auf den Leser wirken. Bitte kein „Bilderbuchdesign“, es soll auf jeden Fall ein reales authentisches Cover (kein Science-Fiction/keine Zeichnung) sein und sich grob an der Idee der ursprünglichen Variante (siehe Anhang 6111.jpeg) orientieren > Titel zentriert oben + Autorname unten, dazwischen die groben Ideen gesammelt zentriert als Eye-Catcher in überschaubarer Größe. Das sind die Vorstellungen, die ich im Kopf habe und ich bin sehr auf die Ergebnisse gespannt.
Bei Fragen gerne vorab melden, sollte die ganze Geschichte vereinfachen - danke schon mal für deine Mühe, ich freue mich sehr auf die Vorschläge!!

```html
<!DOCTYPE html>
<html lang="de">
<head>
<meta charset="utf-8">
<title>Der leise Kompass – Buchcover</title>
<link rel="stylesheet" href="https://fonts.googleapis.com/css2?family=Barlow+Condensed:wght@300;500;700&family=Montserrat:wght@500&display=swap">
<style>
  :root {
    --stage: #e2e2e2;
    --paper: #ececec;
    --paper-light: #f2f2f2;
    --teal-light: #9fd3d3;
    --teal: #4f98a4;
    --navy: #0b2a44;
    --globe-blue: #2f9fd0;
    --globe-green: #5fa046;
    --robe-orange: #e98d17;
    --robe-deep: #b8520f;
  }
  * { margin: 0; padding: 0; box-sizing: border-box; }
  html, body {
    width: 1200px;
    height: 992px;
    overflow: hidden;
    background: var(--stage);
  }
  .stage {
    width: 1200px;
    height: 992px;
    display: flex;
    align-items: center;
    justify-content: center;
  }
  .cover {
    position: relative;
    width: 640px;
    height: 930px;
    background: linear-gradient(180deg, var(--paper-light) 0%, var(--paper) 100%);
    box-shadow: 0 10px 30px rgba(0,0,0,0.12);
    overflow: hidden;
  }
  .title {
    position: absolute;
    top: 60px;
    left: 0;
    right: 0;
    text-align: center;
    font-family: "Barlow Condensed", sans-serif;
    text-transform: uppercase;
    line-height: 0.9;
  }
  .title span {
    display: block;
    -webkit-background-clip: text;
    background-clip: text;
    color: transparent;
  }
  .title-top {
    font-weight: 300;
    font-size: 150px;
    letter-spacing: 2px;
    background-image: linear-gradient(180deg, var(--teal-light) 0%, var(--teal) 100%);
  }
  .title-middle {
    font-weight: 500;
    font-size: 160px;
    letter-spacing: 1px;
    background-image: linear-gradient(180deg, #12506a 0%, var(--navy) 100%);
  }
  .title-bottom {
    font-weight: 700;
    font-size: 158px;
    background-image: linear-gradient(180deg, var(--navy) 0%, #2a7a8a 60%, var(--teal-light) 100%);
  }
  .artwork {
    position: absolute;
    left: 120px;
    top: 500px;
    width: 400px;
    height: 340px;
    border-radius: 50% 50% 40% 40%;
    background:
      radial-gradient(ellipse 42% 38% at 50% 78%, var(--robe-orange) 0%, var(--robe-deep) 60%, rgba(184,82,15,0) 100%),
      radial-gradient(circle at 50% 38%, var(--globe-blue) 0%, var(--globe-green) 45%, rgba(95,160,70,0) 68%);
  }
  .author {
    position: absolute;
    left: 0;
    right: 0;
    bottom: 46px;
    text-align: center;
    font-family: "Montserrat", sans-serif;
    font-weight: 500;
    font-size: 38px;
    letter-spacing: 4px;
    text-transform: uppercase;
    background-image: linear-gradient(90deg, var(--teal-light) 0%, var(--teal) 40%, var(--navy) 100%);
    -webkit-background-clip: text;
    background-clip: text;
    color: transparent;
  }
</style>
</head>
<body>
  <main class="stage">
    <article class="cover">
      <h1 class="title">
        <span class="title-top">Der</span>
        <span class="title-middle">Leise</span>
        <span class="title-bottom">Kompass</span>
      </h1>
      <div class="artwork" role="img" aria-label="Mönch in orangener Robe von hinten vor einer farbigen Weltkugel, umringt von tobenden und zuhörenden Affen"></div>
      <p class="author">Lukas Brenner</p>
    </article>
  </main>
</body>
</html>
```